Web Design for an Online Dating Web Site

We need an uncoded web design for a new online dating web site called zMatchy.net. Simplicity and boldness are the key factors in the successful design.
Please look at the requirements document attached for details.
Updates
Dear all,
Please AVOID USING A PICTURE OF A HAPPY COUPLE ON THE HOME PAGE of the site. We highly want to move away from this space as it makes our web site just like another dating web site.
We like something simple with web 2.0 look and feel. The examples in the Requirements Document are exactly the design we are after.
Regards
Tarn
Industry/Entity Type
Dating
Look and feel
Each slider illustrates characteristics of the customer's brand and the style your logo design should communicate.

```html
<!DOCTYPE html>
<html lang="en">
<head>
<meta charset="utf-8">
<title>zMatchy.net – Home</title>
<link rel="stylesheet" href="https://fonts.googleapis.com/css2?family=Ubuntu:wght@400;500;700&family=Open+Sans:wght@400;600;700&display=swap">
<style>
:root{
  --pink:#e5137f;
  --pink-dark:#9c0c4f;
  --black:#0b0b0b;
  --header:#141414;
  --slider:#ececec;
  --grey-text:#7a7a7a;
  --body-text:#222;
  --footer-text:#e8e8e8;
  --field:#2a2a2a;
}
*{margin:0;padding:0;box-sizing:border-box}
html,body{width:1188px;height:1200px;overflow:hidden}
body{position:relative;background:#fff;font-family:"Open Sans",Arial,sans-serif;color:var(--body-text)}
.abs{position:absolute}

/* header */
.site-header{left:0;top:0;width:1188px;height:37px;background:linear-gradient(#262626,#050505)}
.brand{font-family:"Ubuntu",sans-serif;font-weight:700;color:var(--pink);display:flex;align-items:center;gap:6px}
.brand .dot{width:12px;height:12px;border-radius:50%;background:var(--pink)}
.header-brand{left:297px;top:3px;font-size:25px}
.main-nav{left:478px;top:0;height:37px;display:flex;align-items:center;font-family:"Ubuntu",sans-serif;font-size:8.5px;color:#fff;white-space:nowrap}
.main-nav span{padding:0 5px;border-left:1px solid #444;line-height:20px}
.main-nav span:first-child{color:var(--pink)}
.login-field{top:12px;height:14px;width:62px;background:#e6e6e6;border:1px solid #999;font-size:8px;color:#333;padding-left:4px;line-height:12px}
.login-btn{left:801px;top:12px;width:38px;height:14px;background:#2a2a2a;border:1px solid var(--pink);color:#fff;font-size:8px;text-align:center;line-height:12px}
.more{left:859px;top:13px;color:#fff;font-family:"Ubuntu",sans-serif;font-size:10px;text-align:center;z-index:6}
.more svg{display:block;margin:6px auto 0}
.login-panel{left:777px;top:37px;width:114px;height:119px;background:#111;border-radius:0 0 4px 4px;padding:8px 10px;z-index:5;box-shadow:0 2px 4px rgba(0,0,0,.4)}
.provider{display:flex;align-items:center;gap:6px;height:20px}
.provider i{width:13px;height:13px;display:block}
.provider span{flex:1;height:13px;background:linear-gradient(#fff,#dcdcdc);border-radius:2px;font-size:8px;line-height:13px;padding-left:6px;color:#333}

/* slider */
.slider{left:0;top:37px;width:1188px;height:307px;background:var(--slider);border-bottom:1px solid #cfcfcf}
.slider-arrow{top:176px}
.slider-dots{left:566px;top:351px;display:flex;gap:5px}
.slider-dots i{width:8px;height:8px;border-radius:50%;background:#d6d6d6;border:1px solid #bbb;display:block}
.slider-dots i.on{background:var(--pink-dark)}

/* content */
.content-bg{left:0;top:345px;width:1188px;height:540px;background:linear-gradient(#dcdcdc 0,#fff 300px)}
.section-title{font-family:"Ubuntu",sans-serif;font-weight:400;font-size:16px;color:#222}
.post{left:297px;width:360px;height:100px}
.post-thumb{position:absolute;left:0;top:0;width:130px;height:98px;background:#fff;box-shadow:0 1px 4px rgba(0,0,0,.35);padding:6px}
.post-thumb div{width:100%;height:100%;background:linear-gradient(160deg,#9aa88e,#d8dcc0 55%,#7d8a6a)}
.post-date{position:absolute;left:148px;top:0;font-family:"Ubuntu",sans-serif;font-size:12px;color:var(--grey-text)}
.post-date b{color:#222}
.post-title{position:absolute;left:148px;top:20px;font-family:"Ubuntu",sans-serif;font-weight:500;font-size:16px;color:var(--pink);white-space:nowrap}
.post-body{position:absolute;left:148px;top:44px;width:210px;font-size:8px;line-height:9.5px;color:#222}
.post-link{position:absolute;left:148px;top:89px;font-size:8px;font-style:italic;color:var(--pink)}
.video{left:671px;top:408px;width:220px;height:165px;background:#000;border:1px solid var(--pink)}
.video svg{position:absolute;left:100px;top:68px}
.about-copy{left:671px;width:222px;font-size:8px;line-height:9.5px;color:#222}
.about-copy b{color:var(--pink)}
.about-copy em{color:var(--pink)}
.about-btn{left:671px;top:711px;width:220px;height:28px;background:linear-gradient(#e8408f,#a50d56);border:1px solid #6d0837;color:#fff;font-family:"Ubuntu",sans-serif;font-size:15px;letter-spacing:4px;text-align:center;line-height:26px}
.divider{left:360px;width:470px;height:4px;border-radius:50%;background:radial-gradient(ellipse at center,rgba(0,0,0,.55),rgba(0,0,0,0) 70%)}
.signup-btn{left:471px;top:788px;width:248px;height:49px;background:linear-gradient(#d2377e,#8f0a48);border:1px solid #5e0530;border-radius:3px;box-shadow:0 2px 4px rgba(0,0,0,.35);color:#fff;font-family:"Ubuntu",sans-serif;font-weight:700;font-size:30px;letter-spacing:8px;text-align:center;line-height:47px}

/* footer */
.site-footer{left:0;top:885px;width:1188px;height:315px;background:var(--black)}
.footer-title{font-family:"Ubuntu",sans-serif;font-weight:400;font-size:16px;color:#fff}
.footer-links{left:297px;top:931px;list-style:none;font-size:10px;line-height:13.5px;color:var(--footer-text)}
.footer-links li::before{content:"✦";color:var(--pink);font-size:7px;margin-right:5px}
.social-list{left:483px;top:935px;list-style:none}
.social-list li{display:flex;align-items:center;gap:8px;height:26px;font-family:"Ubuntu",sans-serif;font-size:12px;color:#fff}
.social-list i{width:20px;height:20px;display:block;border-radius:2px}
.field{left:687px;width:204px;background:var(--field);border-radius:2px;font-size:8px;color:#ddd;padding-left:8px;display:flex;align-items:center;gap:8px}
.field.message{align-items:flex-start;padding-top:4px}
.field svg{flex:none}
.submit-btn{left:687px;top:1065px;width:204px;height:18px;background:linear-gradient(#ef3b93,#b70e60);color:#fff;font-family:"Ubuntu",sans-serif;font-size:11px;text-align:center;line-height:18px}
.footer-brand{left:297px;top:1100px;font-size:26px}
.share-row{left:660px;top:1123px;display:flex;align-items:center;gap:6px;font-size:7px;color:#fff}
.share-row .pill{background:#dfe6ef;color:#234;padding:1px 4px;border-radius:2px;font-size:7px}
.share-row .count{background:#fff;color:#111;padding:1px 3px;border:1px solid #bbb;font-size:7px}
.share-row .plus{background:#3d78c9;color:#fff;padding:2px 4px;border-radius:2px;font-weight:700}
.footer-rule{left:297px;top:1156px;width:594px;height:1px;background:#444}
.copyright{left:600px;top:1172px;width:291px;text-align:right;font-size:7px;color:#ddd}
.copyright span{color:var(--pink)}
</style>
</head>
<body>

<header class="site-header abs"></header>
<div class="brand header-brand abs"><i class="dot"></i>zMatchy</div>
<nav class="main-nav abs">
  <span>WHY</span><span>HOW IT WORKS</span><span>BLOG</span><span>SIGN UP</span>
</nav>
<div class="login-field abs" style="left:665px">Username</div>
<div class="login-field abs" style="left:733px">Password</div>
<div class="login-btn abs">LOGIN</div>

<section class="slider abs"></section>
<svg class="slider-arrow abs" style="left:297px" width="18" height="30"><path d="M15 2L3 15l12 13" fill="none" stroke="#222" stroke-width="4"/></svg>
<svg class="slider-arrow abs" style="left:873px" width="18" height="30"><path d="M3 2l12 13L3 28" fill="none" stroke="#222" stroke-width="4"/></svg>
<div class="slider-dots abs"><i></i><i></i><i class="on"></i><i></i><i></i></div>

<div class="login-panel abs">
  <div class="provider"><i style="background:#3b5a9a"></i><span>Friendly</span></div>
  <div class="provider"><i style="background:#c9302c"></i><span>GoMail</span></div>
  <div class="provider"><i style="background:#f08a1c"></i><span>OpenKey</span></div>
  <div class="provider"><i style="background:#2f4f8f"></i><span>OurPlace</span></div>
  <div class="provider"><i style="background:#5a2a85"></i><span>Yodelo</span></div>
</div>
<div class="more abs">MORE<svg width="8" height="5"><path d="M0 0h8L4 5z" fill="#fff"/></svg></div>

<div class="content-bg abs"></div>

<h2 class="section-title abs" style="left:297px;top:374px">Latest Blog Posts</h2>

<article class="post abs" style="top:409px">
  <div class="post-thumb"><div role="img" aria-label="Landscape photo with birds flying over a tree"></div></div>
  <div class="post-date">Jul <b>17</b>, 2011</div>
  <h3 class="post-title">Recent Post Number 1 - Title</h3>
  <p class="post-body">Lorem ipsum dolor sit amet, consectetur adipiscing elit. Etiam at suscipit dui. Sed sollicitudin, libero ac congue condimentum, orci sapien aliquet libero, ut aliquet massa tellus vitae urna.</p>
  <a class="post-link">[ Read the Full Article ]</a>
</article>
<article class="post abs" style="top:525px">
  <div class="post-thumb"><div role="img" aria-label="Landscape photo with birds flying over a tree"></div></div>
  <div class="post-date">Jul <b>10</b>, 2011</div>
  <h3 class="post-title">Recent Post Number 2 - Title</h3>
  <p class="post-body">Lorem ipsum dolor sit amet, consectetur adipiscing elit. Etiam at suscipit dui. Sed sollicitudin, libero ac congue condimentum, orci sapien aliquet libero, ut aliquet massa tellus vitae urna.</p>
  <a class="post-link">[ Read the Full Article ]</a>
</article>
<article class="post abs" style="top:641px">
  <div class="post-thumb"><div role="img" aria-label="Landscape photo with birds flying over a tree"></div></div>
  <div class="post-date">Jul <b>7</b>, 2011</div>
  <h3 class="post-title">Recent Post Number 3 - Title</h3>
  <p class="post-body">Lorem ipsum dolor sit amet, consectetur adipiscing elit. Etiam at suscipit dui. Sed sollicitudin, libero ac congue condimentum, orci sapien aliquet libero, ut aliquet massa tellus vitae urna.</p>
  <a class="post-link">[ Read the Full Article ]</a>
</article>

<h2 class="section-title abs" style="left:671px;top:374px">We are Different</h2>
<div class="video abs"><svg width="24" height="26"><path d="M0 0l24 13L0 26z" fill="var(--pink)"/></svg></div>
<p class="about-copy abs" style="top:591px">In ultricies scelerisque mauris in dignissim. Integer tristique, <b>metus sed tempus consequat</b>, est nulla elementum tellus, quis rhoncus lorem odio vitae augue. Nunc sed est vitae nisi <em>pretium</em> vehicula.</p>
<p class="about-copy abs" style="top:636px">Duis ut mauris nulla, id feugiat diam. <em>Mauris</em> a eros justo. Nunc eget lorem nec tortor varius scelerisque. Quisque venenatis ligula sodales metus suscipit dignissim. Sed vulputate molestie erat, in accumsan dui rutrum a. In vitae purus lacus. Lorem ipsum dolor sit amet, consectetur adipiscing elit.</p>
<div class="about-btn abs">ABOUT US</div>

<div class="divider abs" style="top:772px"></div>
<div class="signup-btn abs">SIGN UP</div>
<div class="divider abs" style="top:847px"></div>

<footer class="site-footer abs"></footer>

<h2 class="footer-title abs" style="left:296px;top:904px">Read More</h2>
<ul class="footer-links abs">
  <li>Why zMatchy</li><li>How it works</li><li>About Us</li><li>Sign Up</li><li>Login</li>
</ul>

<h2 class="footer-title abs" style="left:483px;top:904px">Socialize</h2>
<ul class="social-list abs">
  <li><i style="background:#4fa3d8"></i>CHIRPER</li>
  <li><i style="background:#3b5a9a"></i>FRIENDLY</li>
  <li><i style="background:#4a9a3a"></i>TRIPOVER</li>
  <li><i style="background:#2e6aa8"></i>SCOOPR</li>
  <li><i style="background:#d0d0d0"></i>SAVORY</li>
  <li><i style="background:#2c6f9e"></i>LINKUP</li>
</ul>

<h2 class="footer-title abs" style="left:685px;top:904px">Let’s Talk</h2>
<div class="field abs" style="top:936px;height:17px"><svg width="8" height="9"><circle cx="4" cy="2.5" r="2.3" fill="#ccc"/><path d="M0 9a4 4 0 0 1 8 0z" fill="#ccc"/></svg>Name</div>
<div class="field abs" style="top:960px;height:19px"><svg width="9" height="7"><rect width="9" height="7" fill="#ccc"/><path d="M0 0l4.5 4L9 0" fill="none" stroke="#2a2a2a"/></svg>Email Address</div>
<div class="field message abs" style="top:985px;height:74px">Message</div>
<div class="submit-btn abs">SUBMIT</div>

<div class="brand footer-brand abs"><i class="dot"></i>zMatchy</div>
<div class="share-row abs">
  <span class="plus">+1</span><span class="count">110</span>
  <span class="pill">Chirp</span><span class="count">8,314</span>
  <span class="pill">Like</span><span>999 people like this.</span>
</div>
<div class="footer-rule abs"></div>
<p class="copyright abs">Copyright © 2011 <span>ZMATCHY</span> · All Rights Reserved.</p>

</body>
</html>
```